Modern, profession Order Insert Card for Head Shop/Smoke shop

We are looking for a modern design for our Order Insert cards where we will have some text thanking the customer for their order.
The design needs to be professional and modern, showing our logo (SVG attached) and our website URL.
Our eCommerce store sells "head shop" items, things like bongs, rolling papers, cbd products, disposable vapes, etc.
I have uploaded 2 versions of our logo, one featuring the colour of green we use across our brand, a black logo or the logo can be inverted to be a white logo on a black background.
Target Market(s)
The websites target audience is anyone needing accessories or tools to consume medicinal marijuana/the consumers favourite herbs or any one in the vaping community.
Contact Information for Business Card
Website URL, Space for a small thank you note and our logo.
Look and feel

```html
<!DOCTYPE html>
<html lang="en">
<head>
<meta charset="utf-8">
<title>Leaf and Lantern – Order Insert Card</title>
<link rel="stylesheet" href="https://fonts.googleapis.com/css2?family=Montserrat:wght@500;600;700&family=Satisfy&display=swap">
<style>
  :root {
    --canvas-bg: #e9e4dc;
    --card-light: #ffffff;
    --card-dark: #000000;
    --brush-grey: #f1eff0;
    --brand-green: #1c4a33;
    --ink: #1b1b1b;
    --ink-inverse: #ffffff;
  }
  * { margin: 0; padding: 0; box-sizing: border-box; }
  html, body {
    width: 900px;
    height: 1200px;
    overflow: hidden;
  }
  body {
    position: relative;
    background: var(--canvas-bg);
    font-family: "Montserrat", Arial, sans-serif;
  }
  .card {
    position: absolute;
    left: 82px;
    width: 733px;
    height: 428px;
    border-radius: 22px;
    overflow: hidden;
  }
  .card--front {
    top: 138px;
    background: var(--card-light);
  }
  .card--back {
    top: 634px;
    background: var(--card-dark);
  }
  .brush-wash {
    position: absolute;
    left: 0;
    top: 0;
    width: 733px;
    height: 428px;
  }
  .thanks-script {
    position: absolute;
    left: 182px;
    top: 122px;
    font-family: "Satisfy", cursive;
    font-size: 96px;
    line-height: 1;
    color: var(--brand-green);
    white-space: nowrap;
  }
  .thanks-subline {
    position: absolute;
    left: 209px;
    top: 253px;
    font-size: 14px;
    font-weight: 500;
    letter-spacing: 0.8px;
    color: var(--ink);
  }
  .web-address {
    position: absolute;
    left: 0;
    right: 0;
    top: 356px;
    text-align: center;
    font-size: 15px;
    font-weight: 600;
    letter-spacing: 1.2px;
    color: var(--ink);
  }
  .brand-lockup {
    position: absolute;
    left: 0;
    right: 0;
    top: 0;
    bottom: 0;
    display: flex;
    align-items: center;
    justify-content: center;
    gap: 20px;
  }
  .brand-dot {
    width: 58px;
    height: 58px;
    border-radius: 50%;
    background: var(--ink-inverse);
  }
  .brand-name {
    font-size: 38px;
    font-weight: 700;
    letter-spacing: -0.5px;
    color: var(--ink-inverse);
  }
</style>
</head>
<body>
  <section class="card card--front">
    <svg class="brush-wash" viewBox="0 0 733 428" aria-hidden="true">
      <path fill="var(--brush-grey)" d="M112 100 L240 58 L470 30 L560 20 L580 60 L640 150 L656 250 L670 300 L610 330 L560 380 L420 420 L300 412 L170 398 L110 360 L90 300 L60 240 L100 170 Z"/>
    </svg>
    <p class="thanks-script">Thank you</p>
    <p class="thanks-subline">FOR YOUR PURCHASE</p>
    <p class="web-address">WWW.LEAFANDLANTERN.COM</p>
  </section>

  <section class="card card--back">
    <div class="brand-lockup">
      <span class="brand-dot"></span>
      <span class="brand-name">LEAFANDLANTERN</span>
    </div>
  </section>
</body>
</html>
```